New modern business card design

To design a brand new business card that's clean & modern in terms of layout.
I have attached our company logo and also basic information regarding what is needed on the card that also needs to be editable.

Target Market(s)

motor trade

Contact Information for Business Card

logo, name, title, tel, mob, email, address, www, all information is in the word.doc file

Requirements
Must have
• white background
Nice to have
• Nice clean font

```html
<!DOCTYPE html>
<html lang="en">
<head>
<meta charset="utf-8">
<title>Bolt Rescue Ltd – Business Card</title>
<link href="https://fonts.googleapis.com/css2?family=Roboto:wght@400;500&family=Roboto+Condensed:wght@500;700&display=swap" rel="stylesheet">
<style>
  :root {
    --backdrop: #2b2b2b;
    --card-white: #f4f4f4;
    --brand-blue: #1f6fb6;
    --divider-grey: #9a9a9a;
    --text-light: #ffffff;
  }
  * { margin: 0; padding: 0; box-sizing: border-box; }
  html, body {
    width: 1200px; height: 960px; overflow: hidden;
    background: var(--backdrop);
    font-family: "Roboto", Arial, sans-serif;
  }
  .stage { position: relative; width: 1200px; height: 960px; }

  .card { position: absolute; width: 600px; height: 343px; overflow: hidden; }

  /* Front */
  .card-front { left: 314px; top: 113px; display: flex; background: var(--card-white); }
  .front-brand {
    width: 308px; height: 100%;
    display: flex; align-items: center; justify-content: center; gap: 10px;
  }
  .brand-square { width: 16px; height: 16px; background: var(--brand-blue); }
  .brand-name {
    font-family: "Roboto", Arial, sans-serif; font-weight: 500;
    font-size: 24px; letter-spacing: 1px; color: var(--brand-blue);
    text-transform: uppercase;
  }
  .front-divider { width: 5px; height: 100%; background: var(--divider-grey); border-left: 2px solid var(--card-white); border-right: 1px solid var(--card-white); }
  .front-details {
    flex: 1; background: var(--brand-blue); color: var(--text-light);
    padding: 73px 0 0 33px;
  }
  .person-name {
    font-family: "Roboto Condensed", Arial, sans-serif; font-weight: 700;
    font-size: 23px; line-height: 26px; text-transform: uppercase;
  }
  .person-title {
    font-family: "Roboto Condensed", Arial, sans-serif; font-weight: 500;
    font-size: 16px; line-height: 20px; text-transform: uppercase; margin-bottom: 10px;
  }
  .address { font-style: normal; font-size: 15px; line-height: 18px; margin-bottom: 8px; }
  .contact-list { list-style: none; font-size: 15px; line-height: 19px; }
  .contact-list li { display: flex; align-items: center; gap: 8px; }
  .contact-list svg { width: 14px; height: 14px; fill: var(--text-light); flex: none; }

  /* Back */
  .card-back {
    left: 311px; top: 472px; background: var(--brand-blue); color: var(--text-light);
    display: flex; flex-direction: column; align-items: center;
  }
  .back-brand {
    margin-top: 128px; height: 70px;
    display: flex; align-items: center; gap: 16px;
  }
  .back-brand .brand-square { width: 28px; height: 28px; background: var(--text-light); }
  .back-brand .brand-name { font-size: 42px; color: var(--text-light); }
  .back-web {
    position: absolute; top: 288px; width: 100%; text-align: center;
    font-size: 15px; letter-spacing: 4.5px;
  }
</style>
</head>
<body>
<main class="stage">
  <section class="card card-front">
    <div class="front-brand">
      <span class="brand-square"></span>
      <span class="brand-name">Bolt Rescue Ltd</span>
    </div>
    <div class="front-divider"></div>
    <div class="front-details">
      <h1 class="person-name">Daniel Harper</h1>
      <p class="person-title">General Manager</p>
      <address class="address">Kestrel Street<br>Fairholme, Manchester<br>M41 2QT</address>
      <ul class="contact-list">
        <li><svg viewBox="0 0 24 24"><path d="M6.6 10.8a15.1 15.1 0 0 0 6.6 6.6l2.2-2.2a1 1 0 0 1 1-.25 11.4 11.4 0 0 0 3.6.57 1 1 0 0 1 1 1V20a1 1 0 0 1-1 1A17 17 0 0 1 3 4a1 1 0 0 1 1-1h3.5a1 1 0 0 1 1 1c0 1.25.2 2.45.57 3.57a1 1 0 0 1-.25 1z"/></svg>0161 555 0142</li>
        <li><svg viewBox="0 0 24 24"><path d="M7 1h10a2 2 0 0 1 2 2v18a2 2 0 0 1-2 2H7a2 2 0 0 1-2-2V3a2 2 0 0 1 2-2zm0 3v14h10V4zm5 15.5a1 1 0 1 0 0 2 1 1 0 0 0 0-2z"/></svg>07700 900 418</li>
        <li><svg viewBox="0 0 24 24"><path d="M2 5h20v14H2zm2 2v.5l8 5 8-5V7zm0 2.8V17h16V9.8l-8 5z"/></svg>dharper@bolt-rescue.co.uk</li>
        <li><svg viewBox="0 0 24 24"><path d="M12 2a10 10 0 1 0 0 20 10 10 0 0 0 0-20zm-1 17.9A8 8 0 0 1 4.2 10.2L9 15v1a2 2 0 0 0 2 2zm6.9-2.5A2 2 0 0 0 16 16h-1v-3a1 1 0 0 0-1-1H8v-2h2a1 1 0 0 0 1-1V7h2a2 2 0 0 0 2-2v-.4a8 8 0 0 1 2.9 12.8z"/></svg>www.bolt-rescue.co.uk</li>
      </ul>
    </div>
  </section>

  <section class="card card-back">
    <div class="back-brand">
      <span class="brand-square"></span>
      <span class="brand-name">Bolt Rescue</span>
    </div>
    <p class="back-web">www.bolt-rescue.co.uk</p>
  </section>
</main>
</body>
</html>
```